Engineering Consultant Business Card

I'm starting a new business as a high-end engineering consultant in a niche field. I've attached the jpg for my logo plus the branding guideline document that I've been following. You can see my business website here: www.orvalink.com
I'd like a business card that has the logo on one side, then the other side has (in any order): Tessmor Pact, Inc.
Delia Whitcombe
President and Chief EMC Engineer
www.orvalink.com
delia@orvalink.com
Optional: motto "We will solve your EMC problems as early as possible—ideally before they even start."
I'm not planning on including a phone number
Target Market(s)
Businesses, especially makers of electronics hardware
Industry/Entity Type
Electrical engineering
Contact Information for Business Card
Company name, my name, website, email
Look and feel
Each slider illustrates characteristics of the customer's brand and the style your logo design should communicate.

```html
<!DOCTYPE html>
<html lang="en">
<head>
<meta charset="utf-8">
<title>Tessmor Pact, Inc. — Business Card</title>
<link href="https://fonts.googleapis.com/css2?family=Montserrat:wght@400;500;700&display=swap" rel="stylesheet">
<style>
  :root {
    --bg: #1d1e22;
    --card-blue: #2c44a6;
    --paper: #ffffff;
    --accent-cyan: #4cc0e4;
    --text-light: #e9edfb;
    --mark-soft: #4a62c4;
  }
  * { margin: 0; padding: 0; box-sizing: border-box; }
  html, body {
    width: 1200px; height: 900px; overflow: hidden;
    background: var(--bg);
    font-family: "Montserrat", sans-serif;
  }
  .canvas {
    width: 1200px; height: 900px;
    display: flex; align-items: center; justify-content: center; gap: 60px;
  }
  .card {
    position: relative;
    width: 525px; height: 300px;
    border-radius: 6px;
    overflow: hidden;
    background: var(--card-blue);
    box-shadow: 0 18px 40px rgba(0,0,0,.45);
  }
  /* Front: contact side */
  .card-front .sweep {
    position: absolute; inset: 0; width: 100%; height: 100%;
  }
  .contact {
    position: absolute; left: 30px; top: 30px;
    color: var(--text-light);
  }
  .contact-name {
    color: var(--accent-cyan);
    font-weight: 700; font-size: 17px; letter-spacing: .5px;
    text-transform: uppercase;
  }
  .contact-title {
    font-size: 14px; line-height: 1.3; margin-top: 4px;
  }
  .contact-rule {
    width: 14px; height: 1.5px; background: var(--accent-cyan);
    margin: 10px 0 8px;
  }
  .contact-list { list-style: none; font-size: 14px; line-height: 1.55; }
  .contact-list li { display: flex; align-items: center; gap: 8px; }
  .contact-list svg { width: 11px; height: 11px; flex: none; }
  .brand-front {
    position: absolute; left: 326px; top: 196px;
    display: flex; align-items: center; gap: 9px;
    color: var(--card-blue);
    font-weight: 700; font-size: 18px; letter-spacing: 1px;
    text-transform: uppercase; white-space: nowrap;
  }
  .brand-dot {
    width: 14px; height: 14px; border-radius: 50%;
    background: var(--card-blue); flex: none;
  }
  /* Back: brand side */
  .card-back {
    display: flex; flex-direction: column; align-items: center; justify-content: center;
    gap: 28px;
  }
  .brand-back {
    display: flex; align-items: center; gap: 12px;
    color: var(--mark-soft);
    font-weight: 700; font-size: 30px; letter-spacing: 2px;
    text-transform: uppercase; white-space: nowrap;
  }
  .brand-back .brand-dot { width: 22px; height: 22px; background: var(--mark-soft); }
  .motto {
    color: var(--text-light);
    font-size: 13px; line-height: 1.45; text-align: center;
  }
</style>
</head>
<body>
<main class="canvas">
  <section class="card card-front" aria-label="Business card front">
    <svg class="sweep" viewBox="0 0 525 300" aria-hidden="true">
      <circle cx="470" cy="300" r="215" fill="none" stroke="#ffffff" stroke-width="3"/>
      <circle cx="470" cy="300" r="205" fill="#ffffff"/>
    </svg>
    <div class="contact">
      <h1 class="contact-name">Delia Whitcombe</h1>
      <p class="contact-title">President and Chief<br>EMC Engineer</p>
      <div class="contact-rule"></div>
      <ul class="contact-list">
        <li>
          <svg viewBox="0 0 12 12"><rect x="1" y="2.5" width="10" height="7" rx="1" fill="#4cc0e4"/><path d="M1.5 3l4.5 3.5L10.5 3" fill="none" stroke="#2c44a6" stroke-width="1"/></svg>
          delia@orvalink.com
        </li>
        <li>
          <svg viewBox="0 0 12 12"><circle cx="6" cy="6" r="5" fill="#4cc0e4"/><path d="M1 6h10M6 1c2 2.5 2 7.5 0 10M6 1c-2 2.5-2 7.5 0 10" fill="none" stroke="#2c44a6" stroke-width=".8"/></svg>
          www.orvalink.com
        </li>
      </ul>
    </div>
    <div class="brand-front">
      <span class="brand-dot"></span>
      <span>Tessmor Pact</span>
    </div>
  </section>

  <section class="card card-back" aria-label="Business card back">
    <div class="brand-back">
      <span class="brand-dot"></span>
      <span>Tessmor Pact</span>
    </div>
    <p class="motto">We will solve your EMC problems as early as possible<br>ideally before they even start</p>
  </section>
</main>
</body>
</html>
```